Business Card Design

An energy company designed around renewable energy and energy storage that focuses on providing its energy at points on the grid that reduce costs and add value to the system.

Industry/Entity Type

Business

Contact Information for Business Card

Martin Delacroix
Executive Vice President
41 K ST NE
Washington, DC 20017
240-555-0183
mdelacroix@harborvoltco.example

```html
<!DOCTYPE html>
<html lang="en">
<head>
<meta charset="utf-8">
<title>Martin Delacroix – Business Cards</title>
<link rel="stylesheet" href="https://fonts.googleapis.com/css2?family=Roboto+Condensed:wght@400;500&display=swap">
<style>
  :root {
    --backdrop: #ececec;
    --card: #ffffff;
    --card-edge: #e3e4e4;
    --ink: #1c1c1c;
    --title-ink: #2a2a2a;
    --name-ink: #ffffff;
    --green: #17a84b;
    --green-deep: #0e7a38;
    --red: #ea2229;
    --red-deep: #a8181d;
    --band-shadow: rgba(0, 0, 0, 0.14);
  }
  * { box-sizing: border-box; margin: 0; padding: 0; }
  html, body {
    width: 1200px;
    height: 1000px;
    overflow: hidden;
    background: var(--backdrop);
    font-family: "Roboto Condensed", "Arial Narrow", sans-serif;
  }
  .sheet {
    width: 1200px;
    height: 1000px;
    display: flex;
    flex-direction: column;
    align-items: center;
    justify-content: center;
    gap: 60px;
  }
  .business-card {
    position: relative;
    width: 700px;
    height: 400px;
    background: var(--card);
    border: 9px solid var(--card-edge);
    box-shadow: 0 6px 18px rgba(0, 0, 0, 0.12);
  }
  .business-card--green { --accent: var(--green); --accent-deep: var(--green-deep); }
  .business-card--red { --accent: var(--red); --accent-deep: var(--red-deep); }

  .name-band {
    position: absolute;
    left: 22px;
    top: 168px;
    width: 300px;
    height: 92px;
    background: var(--accent);
    padding: 12px 0 0 14px;
    box-shadow: 0 7px 0 var(--band-shadow);
  }
  .name-band__fold {
    position: absolute;
    left: -22px;
    top: 0;
    width: 22px;
    height: 108px;
    background: var(--accent-deep);
    clip-path: polygon(0 12px, 100% 0, 100% 92px, 0 100%);
  }
  .name-band__name {
    font-size: 36px;
    font-weight: 400;
    color: var(--name-ink);
    line-height: 1;
    letter-spacing: 0.2px;
  }
  .name-band__title {
    margin-top: 6px;
    font-size: 22px;
    color: var(--title-ink);
    line-height: 1;
  }
  .contact {
    position: absolute;
    left: 340px;
    top: 164px;
    font-size: 22px;
    font-weight: 500;
    line-height: 1.32;
    color: var(--ink);
    list-style: none;
  }
</style>
</head>
<body>
  <main class="sheet">
    <article class="business-card business-card--green">
      <div class="name-band">
        <span class="name-band__fold"></span>
        <h1 class="name-band__name">Martin Delacroix</h1>
        <p class="name-band__title">Executive Vice President</p>
      </div>
      <ul class="contact">
        <li>240-555-0183</li>
        <li>mdelacroix@harborvoltco.example</li>
        <li>41 K ST NE Washington, DC 20017</li>
      </ul>
    </article>

    <article class="business-card business-card--red">
      <div class="name-band">
        <span class="name-band__fold"></span>
        <h2 class="name-band__name">Martin Delacroix</h2>
        <p class="name-band__title">Executive Vice President</p>
      </div>
      <ul class="contact">
        <li>240-555-0183</li>
        <li>mdelacroix@harborvoltco.example</li>
        <li>41 K ST NE Washington, DC 20017</li>
      </ul>
    </article>
  </main>
</body>
</html>
```